Business Card Design Project

Design business card based on logo provided.

Industry/Entity Type

Business

Requirements
Nice to have
• Logo to be provided.

Solid green second side with reverse logo (buildings only, not text).

Because the logo is linear I think that it might be possible to extend the logo lines across the card (only on the second side) as an interesting design element.

"Helping Owners Build Better Building Programs"

"Job Order Contracting and Best Value Specialist"

"Cooperation - Innovation - Efficiency"

Basic Info:
Nora Whitfield
Owner/Founder
505-718-6024
nora@norawhitfieldpartners.example

www.norawhitfieldpartners.example (this should probably be on reverse)

```html
<!DOCTYPE html>
<html lang="en">
<head>
<meta charset="utf-8">
<title>Nora Whitfield Partners – Business Cards</title>
<link href="https://fonts.googleapis.com/css2?family=Oswald:wght@400&family=Quicksand:wght@400;500&display=swap" rel="stylesheet">
<style>
  :root {
    --lime: #cddf36;
    --white: #ffffff;
    --card-border: #8a8a8a;
    --page: #ffffff;
  }
  html, body {
    margin: 0;
    padding: 0;
    width: 1200px;
    height: 900px;
    overflow: hidden;
    background: var(--page);
  }
  .canvas {
    position: relative;
    width: 1200px;
    height: 900px;
  }
  .card {
    position: absolute;
    left: 296px;
    width: 648px;
    height: 372px;
    box-sizing: border-box;
    overflow: hidden;
  }
  .card--front {
    top: 56px;
    background: var(--lime);
  }
  .card--back {
    top: 490px;
    background: var(--white);
    border: 2px solid var(--card-border);
  }

  /* Front */
  .front-mark {
    position: absolute;
    left: 160px;
    top: 234px;
    width: 42px;
    height: 42px;
    box-sizing: border-box;
    border: 5px solid var(--white);
  }
  .card--front .brand-name {
    position: absolute;
    left: 220px;
    top: 234px;
    margin: 0;
    font-family: "Oswald", sans-serif;
    font-weight: 400;
    font-size: 35px;
    line-height: 42px;
    letter-spacing: 0.3px;
    color: var(--white);
    text-transform: uppercase;
    white-space: nowrap;
  }
  .front-tagline {
    position: absolute;
    left: 44px;
    top: 318px;
    margin: 0;
    font-family: "Quicksand", sans-serif;
    font-weight: 400;
    font-size: 27px;
    line-height: 1;
    color: var(--white);
    text-transform: uppercase;
    white-space: nowrap;
  }

  /* Back */
  .back-brand {
    position: absolute;
    left: 52px;
    top: 92px;
    width: 150px;
  }
  .back-brand .brand-square {
    display: block;
    width: 40px;
    height: 40px;
    box-sizing: border-box;
    border: 5px solid var(--lime);
    margin-bottom: 14px;
  }
  .back-brand .brand-name {
    margin: 0;
    font-family: "Quicksand", sans-serif;
    font-weight: 500;
    font-size: 20px;
    line-height: 1.3;
    color: var(--lime);
  }
  .contact {
    position: absolute;
    left: 214px;
    top: 152px;
    margin: 0;
    font-family: "Quicksand", sans-serif;
    font-weight: 400;
    color: var(--lime);
    font-style: normal;
  }
  .contact__name {
    display: block;
    font-size: 28px;
    line-height: 1;
    margin-bottom: 14px;
  }
  .contact__line {
    display: block;
    font-size: 22px;
    line-height: 30px;
    white-space: nowrap;
  }
  .back-tagline {
    position: absolute;
    left: 52px;
    top: 320px;
    margin: 0;
    font-family: "Quicksand", sans-serif;
    font-weight: 400;
    font-size: 23px;
    line-height: 1;
    color: var(--lime);
    white-space: nowrap;
  }
</style>
</head>
<body>
<main class="canvas">

  <section class="card card--front" aria-label="Card front">
    <span class="front-mark" aria-hidden="true"></span>
    <h1 class="brand-name">Nora Whitfield Partners</h1>
    <p class="front-tagline">Cooperation - Innovation - Efficiency</p>
  </section>

  <section class="card card--back" aria-label="Card back">
    <div class="back-brand">
      <span class="brand-square" aria-hidden="true"></span>
      <p class="brand-name">Nora<br>Whitfield<br>Partners</p>
    </div>
    <address class="contact">
      <span class="contact__name">Nora Whitfield</span>
      <span class="contact__line">Owner/Founder</span>
      <span class="contact__line">505-718-6024</span>
      <span class="contact__line">nora@norawhitfieldpartners.example</span>
    </address>
    <p class="back-tagline">Helping Owners Build Better Building Programs</p>
  </section>

</main>
</body>
</html>
```